Lanterby Ridge Partners

We are a Private Equity firm that works with small companies. We have a mission of working with companies that help others in some way, shape, or form. If we feel that there is not a definitive way that the business helps others, we initiate a program of giving to others.

Target Market(s)

Our target market is small to mid size businesses. We do not have a certain business sector that we go after, but work with companies that have a niche.

Contact Information for Business Card

Currently very plain, black and white, standard print

Logo Text

Dedicated to Success

Requirements
Must have
• Want the color(s) and scheme to give off the feeling of openness to change, smart and sharp look, with a monogrammed type logo
Nice to have
• It would be nice to have a simple and look of distinction. We operate the Private Equity Firm as a virtual office and bring in best in class partners to work on projects as partners.
Should not have
• A wild and out of touch look.

```html
<!DOCTYPE html>
<html lang="en">
<head>
<meta charset="utf-8">
<title>Lanterby Ridge Partners – Business Card</title>
<link href="https://fonts.googleapis.com/css2?family=Montserrat:wght@600&family=Roboto:wght@400&display=swap" rel="stylesheet">
<style>
  :root {
    --backdrop: #b9b6b9;
    --card: #f4f4f3;
    --ink: #1d1d1f;
    --brand-blue: #1a8fd6;
    --deep-blue: #1f5fae;
    --band: #dedede;
  }
  html, body {
    margin: 0;
    width: 1200px;
    height: 1012px;
    overflow: hidden;
    background: var(--backdrop);
  }
  .business-card {
    position: absolute;
    left: 100px;
    top: 220px;
    width: 1000px;
    height: 572px;
    background: var(--card);
    box-shadow: 0 10px 30px rgba(0,0,0,0.18);
    overflow: hidden;
  }
  .brand {
    position: absolute;
    left: 50px;
    top: 256px;
    display: flex;
    align-items: center;
    gap: 18px;
  }
  .brand-mark {
    width: 50px;
    height: 50px;
    border-radius: 50%;
    background: var(--deep-blue);
    flex: none;
  }
  .brand-name {
    font-family: "Montserrat", sans-serif;
    font-weight: 600;
    font-size: 31px;
    color: var(--ink);
    letter-spacing: 0.3px;
    white-space: nowrap;
  }
  .holder-name {
    position: absolute;
    left: 580px;
    top: 120px;
    margin: 0;
    font-family: "Roboto", sans-serif;
    font-weight: 400;
    font-size: 42px;
    color: var(--brand-blue);
    white-space: nowrap;
  }
  .contact-band {
    position: absolute;
    left: 610px;
    top: 190px;
    width: 44px;
    height: 260px;
    background: var(--band);
  }
  .contact-list {
    position: absolute;
    left: 610px;
    top: 230px;
    margin: 0;
    padding: 0;
    list-style: none;
    font-family: "Roboto", sans-serif;
    font-size: 23px;
    line-height: 30px;
    color: var(--ink);
  }
  .contact-item {
    display: flex;
    align-items: flex-start;
    gap: 18px;
    margin-bottom: 20px;
    white-space: nowrap;
  }
  .contact-icon {
    width: 44px;
    height: 40px;
    background: var(--brand-blue);
    display: flex;
    align-items: center;
    justify-content: center;
    flex: none;
  }
  .contact-icon svg { width: 22px; height: 22px; }
  .contact-text { padding-top: 5px; }
</style>
</head>
<body>
  <div class="business-card">
    <div class="brand">
      <span class="brand-mark"></span>
      <span class="brand-name">Lanterby Ridge Partners</span>
    </div>

    <h1 class="holder-name">Daniel Hartley</h1>

    <div class="contact-band"></div>
    <ul class="contact-list">
      <li class="contact-item">
        <span class="contact-icon">
          <svg viewBox="0 0 24 24" aria-hidden="true"><path fill="#fff" d="M6.6 10.8a15.1 15.1 0 0 0 6.6 6.6l2.2-2.2c.3-.3.7-.4 1-.2 1.1.4 2.3.6 3.6.6.6 0 1 .4 1 1V20c0 .6-.4 1-1 1A17 17 0 0 1 3 4c0-.6.4-1 1-1h3.5c.6 0 1 .4 1 1 0 1.3.2 2.5.6 3.6.1.3 0 .7-.2 1z"/></svg>
        </span>
        <span class="contact-text">555 018 2047</span>
      </li>
      <li class="contact-item">
        <span class="contact-icon">
          <svg viewBox="0 0 24 24" aria-hidden="true"><path fill="#fff" d="M3 6h18v12H3z"/><path fill="none" stroke="#1a8fd6" stroke-width="1.8" d="M3 6l9 7 9-7"/></svg>
        </span>
        <span class="contact-text">hartley@lanterbyridge.com</span>
      </li>
      <li class="contact-item">
        <span class="contact-icon">
          <svg viewBox="0 0 24 24" aria-hidden="true"><path fill="#fff" d="M12 2a7 7 0 0 0-7 7c0 5.2 7 13 7 13s7-7.8 7-13a7 7 0 0 0-7-7zm0 9.5A2.5 2.5 0 1 1 12 6.5a2.5 2.5 0 0 1 0 5z"/></svg>
        </span>
        <span class="contact-text">Address Line 1<br>Address Line 2<br>Address Line 3</span>
      </li>
    </ul>
  </div>
</body>
</html>
```